Bright Path Flyer Design for Virtual Online Clinic. -5.5 x 8.5 inches (half sheet)

We need a clean, modern flyer design for Bright Path, a new virtual walk-in clinic based in British Columbia. The flyer will be used in libraries, pharmacies, and community centers to help residents easily access primary care through their Bright Path NFC access card.
The flyer will ask a question : NEED A DOCTOR? This should be large and attention grabbing.
The design should clearly feature a Bright Path card image (the access card) as the centerpiece and visually show how patients can use it to book appointments. The tone should feel trustworthy, healthcare-oriented, and community-friendly — clean fonts, clear spacing, and strong readability from a distance.

Side One: This card has the NFC Access Card.
NEED A DOCTOR? (Large Font, Attention Grabbing)
How to Book an Appointment using your Bright Path Card
Step 1: Tap Your Card on Your Phone
Hold your card near the back of your phone.
It will activate automatically — no app needed.
The Bright Path scheduler will open.
Step 2: Schedule Your Appointment
Select your clinical concern.
Choose your time window.
Register (only once).
Confirm your appointment.
Step 3: Relax, we’ll take care of the rest
A doctor will call during your scheduled time.
Once booked, you’ll be able to call our office.
No emails, no texts — just a real person.
It’s that simple.
Side Two:
About Bright Path
Created by Dr. Marcus Ferrigan
Bright Path was founded to make healthcare simple and convenient. Prescription renewals. Common infections. Medical notes. And so much more.
Our doctors can address 120+ health concerns virtually — providing quality care without the waiting room. No waiting rooms. Just real doctors providing real care.
Why Patients Choose Bright Path
Easy access – book and be seen from anywhere in BC.
Effortless booking – tap your Bright Path Card to begin.
Trusted physicians – every visit is with a licensed BC family doctor.
How It Works
Book your visit — choose a time window that fits your day.
Join the queue — you’ll be called when it’s your turn.
Speak directly with your doctor — simple, secure, and stress-free.
Convenient Care for Common Concerns

Additional Details.
Please find the domain to be launched soon. I've attached the NFC card file for review, it is 85.5 mm x 54 mm. The card will be glued to the flyer.
I've attached examples of flyers but they are not the look I am seeking and I am looking for creative solutions.
Thank you!
http://brightpath-example.test/

Adult Patients in British Columbia

Healthcare

• Looking for clean lines, uniform appearance, and high legibility i.e poppins

0054AA
0677BA
7BADD7
CADEEF
E8F1F8

• Need A Doctor?
• Elegant style, not too busy, clear layout.
• Clutter, look cheap - review examples.

```html
<!DOCTYPE html>
<html lang="en">
<head>
<meta charset="UTF-8">
<title>Bright Path Flyer – Front and Back</title>
<link rel="stylesheet" href="https://fonts.googleapis.com/css2?family=Poppins:ital,wght@0,400;0,500;0,600;0,700;0,800;1,500;1,600&display=swap">
<style>
  :root {
    --navy: #0054AA;
    --deep: #1d3f8f;
    --blue: #0677BA;
    --sky: #7BADD7;
    --mist: #CADEEF;
    --ice: #E8F1F8;
    --ink: #222833;
    --white: #ffffff;
    --stage: #e4e4e4;
  }
  * { box-sizing: border-box; margin: 0; padding: 0; }
  html, body { width: 1200px; height: 1137px; overflow: hidden; }
  body {
    background: var(--stage);
    font-family: "Poppins", Arial, sans-serif;
    color: var(--ink);
    position: relative;
  }
  .page {
    position: absolute;
    top: 167px;
    width: 514px;
    height: 796px;
    background: var(--white);
    box-shadow: 0 3px 12px rgba(0,0,0,.18);
    overflow: hidden;
  }
  .page--front { left: 65px; background: linear-gradient(180deg, #f4f8fc 0%, #ffffff 40%); }
  .page--back { left: 615px; }
  .abs { position: absolute; }

  /* Front */
  .headline {
    left: 0; right: 0; top: 22px;
    text-align: center;
    font-weight: 800;
    font-size: 51px;
    letter-spacing: -0.5px;
    color: var(--navy);
    line-height: 1;
  }
  .headline-rule {
    left: 35px; right: 35px; top: 77px;
    height: 2px; background: var(--navy);
  }
  .subhead {
    left: 0; right: 0; top: 85px;
    text-align: center;
    font-size: 16px;
    line-height: 24px;
    color: var(--ink);
  }
  .subhead strong { font-weight: 700; color: var(--deep); }
  .card-visual {
    left: 0; top: 150px; width: 440px; height: 360px;
    border-radius: 0 120px 60px 0;
    background: linear-gradient(135deg, #f1d7c8 0%, #e7c2ad 35%, #2a4d9c 60%, #e9eef7 100%);
    opacity: .9;
  }
  .front-wave { left: 0; top: 0; width: 514px; height: 796px; }
  .steps { left: 0; top: 556px; width: 400px; }
  .step {
    position: absolute; left: 20px; width: 400px;
    display: flex; gap: 16px; color: var(--white);
  }
  .step-num {
    flex: none; width: 38px; height: 38px; border-radius: 50%;
    background: var(--blue);
    display: flex; align-items: center; justify-content: center;
    font-weight: 600; font-size: 20px;
    box-shadow: 0 0 0 3px rgba(123,173,215,.35);
  }
  .step-title { font-weight: 700; font-size: 13px; line-height: 17px; }
  .step-text { font-size: 12.5px; line-height: 16px; color: #eaf1f9; }
  .tagline {
    left: 390px; top: 680px; width: 190px; height: 190px;
    border-radius: 50%;
    background: radial-gradient(circle at 40% 40%, #ffffff 60%, var(--mist) 100%);
    padding: 30px 0 0 26px;
    font-style: italic; font-weight: 600;
    font-size: 21px; line-height: 28px;
    color: var(--blue);
  }

  /* Back */
  .back-art { left: 0; top: 0; width: 514px; height: 796px; }
  .back-title {
    left: 25px; top: 12px;
    font-weight: 600; font-size: 26px; color: var(--white);
  }
  .back-title-rule { left: 25px; top: 51px; width: 272px; height: 1px; background: rgba(255,255,255,.7); }
  .byline { left: 25px; top: 52px; font-style: italic; font-size: 13.5px; color: var(--white); }
  .photo-slot {
    left: 408px; top: 14px; width: 82px; height: 196px;
    border-radius: 12px;
    background: linear-gradient(160deg, #3b4350 0%, #dfe8f1 40%, #ffffff 70%, #c9d4e0 100%);
  }
  .mission { left: 78px; top: 164px; width: 320px; border-left: 3px solid var(--blue); padding-left: 10px; }
  .mission h2 { font-size: 17px; font-weight: 600; color: var(--blue); line-height: 24px; margin-bottom: 4px; }
  .mission p { font-size: 12.8px; line-height: 17.5px; color: var(--ink); white-space: nowrap; }
  .why {
    left: 0; right: 0; top: 290px; text-align: center;
    font-size: 17px; font-weight: 600; color: var(--blue);
  }
  .benefit {
    position: absolute; top: 355px; width: 148px; height: 124px;
    background: var(--ice); border-radius: 4px;
    box-shadow: 0 2px 4px rgba(0,0,0,.08);
    text-align: center; padding-top: 38px;
  }
  .benefit-icon {
    position: absolute; left: 50%; top: -30px; margin-left: -27px;
    width: 54px; height: 54px; border-radius: 50%;
    background: var(--white); border: 2px solid var(--blue);
    display: flex; align-items: center; justify-content: center;
  }
  .benefit h3 { font-size: 13px; font-weight: 600; color: var(--ink); line-height: 18px; }
  .benefit p { font-size: 12px; line-height: 15.5px; color: #3a404a; margin-top: 2px; }
  .howbox { left: 25px; top: 507px; width: 464px; height: 175px; }
  .howbox-lead {
    position: absolute; left: 0; top: 0; width: 148px; height: 175px;
    background: var(--deep); color: var(--white);
    text-align: right; padding: 20px 14px 0 8px;
  }
  .howbox-lead .kicker { font-weight: 700; font-size: 15px; line-height: 17px; text-transform: uppercase; }
  .howbox-lead .kicker span { color: #3ea0e6; }
  .howbox-lead .big { font-size: 19px; margin-top: 8px; line-height: 22px; }
  .howbox-lead .small { font-size: 12.5px; line-height: 15px; }
  .howbox-tab {
    position: absolute; left: 148px; top: 0; width: 35px; height: 175px;
    background: var(--blue); border-radius: 0 4px 4px 0;
    display: flex; align-items: center; justify-content: center;
  }
  .howbox-tab span { transform: rotate(-90deg); white-space: nowrap; color: var(--white); font-weight: 600; font-size: 14px; }
  .howbox-list {
    position: absolute; left: 183px; top: 0; width: 281px; height: 175px;
    background: linear-gradient(90deg, var(--ice), #ffffff);
  }
  .how-step { position: absolute; left: 16px; width: 252px; display: flex; gap: 10px; }
  .how-step .step-num { width: 28px; height: 28px; font-size: 15px; color: var(--white); box-shadow: none; }
  .how-step h4 { font-size: 12.5px; font-weight: 600; color: var(--deep); line-height: 16px; }
  .how-step p { font-size: 12.5px; line-height: 17px; color: var(--ink); }
  .how-rule { position: absolute; left: 48px; width: 220px; border-top: 1.5px dotted var(--blue); }
  .brand-mark {
    left: 25px; top: 728px;
    font-size: 28px; font-weight: 500; color: var(--deep);
  }
  .contact {
    left: 255px; top: 740px; font-size: 12px; line-height: 18px;
    color: var(--deep); font-weight: 500; white-space: nowrap;
  }
</style>
</head>
<body>

<section class="page page--front">
  <h1 class="abs headline">NEED A DOCTOR?</h1>
  <div class="abs headline-rule"></div>
  <p class="abs subhead">This card gives you instant access to <strong>virtual care</strong><br>— anywhere in BC.</p>

  <div class="abs card-visual" role="img" aria-label="Photo of a hand holding the Bright Path NFC access card"></div>

  <svg class="abs front-wave" viewBox="0 0 514 796" aria-hidden="true">
    <defs>
      <linearGradient id="frontBand" x1="0" y1="0" x2="1" y2="1">
        <stop offset="0" stop-color="#0677BA"/>
        <stop offset="1" stop-color="#1d3f8f"/>
      </linearGradient>
    </defs>
    <path d="M0 520 C 170 560, 380 470, 514 370 L514 380 C 380 490, 170 580, 0 548 Z" fill="#0677BA"/>
    <path d="M0 548 C 170 580, 380 490, 514 390 L514 796 L0 796 Z" fill="url(#frontBand)"/>
  </svg>

  <div class="abs steps">
    <div class="step" style="top:0">
      <div class="step-num">1</div>
      <div>
        <div class="step-title">Tap Your Card on Your Phone</div>
        <div class="step-text">Hold your card near the back of your phone.<br>It will activate automatically — no app needed.</div>
      </div>
    </div>
    <div class="step" style="top:72px">
      <div class="step-num">2</div>
      <div>
        <div class="step-title">Schedule Your Appointment</div>
        <div class="step-text">Select your concern, choose your time window,<br>Register (only once) and confirm.</div>
      </div>
    </div>
    <div class="step" style="top:146px">
      <div class="step-num">3</div>
      <div>
        <div class="step-title">Relax, We'l Take Care of The Rest</div>
        <div class="step-text">A doctor will call you during your scheduled time<br>Once booked, you'll be able to call our office.<br>No emails, no texts — just a real person.</div>
      </div>
    </div>
  </div>

  <div class="abs tagline">It's that<br>Simple</div>
</section>

<section class="page page--back">
  <svg class="abs back-art" viewBox="0 0 514 796" aria-hidden="true">
    <defs>
      <linearGradient id="backBand" x1="0" y1="0" x2="1" y2="0">
        <stop offset="0" stop-color="#1d3f8f"/>
        <stop offset="1" stop-color="#0054AA"/>
      </linearGradient>
    </defs>
    <path d="M0 0 H514 V95 C 380 85, 200 80, 0 150 Z" fill="url(#backBand)"/>
    <path d="M0 170 C 110 100, 260 80, 380 100 L380 106 C 260 90, 110 112, 0 182 Z" fill="#0677BA"/>
  </svg>

  <h1 class="abs back-title">About Bright Path</h1>
  <div class="abs back-title-rule"></div>
  <p class="abs byline">Created by Dr. Marcus Ferrigan</p>

  <div class="abs photo-slot" role="img" aria-label="Photo of a doctor holding a stethoscope out of a smartphone screen"></div>

  <div class="abs mission">
    <h2>Our Mission</h2>
    <p>Bright Path was founded to make<br>healthcare simple and convenient.<br>Our doctors can address 120+ health concerns<br>virtually — from prescriptions to medical notes.*</p>
  </div>

  <h2 class="abs why">Why Patients Choose Bright Path</h2>

  <div class="benefit" style="left:25px">
    <div class="benefit-icon">
      <svg width="28" height="28" viewBox="0 0 28 28" fill="none" stroke="#0677BA" stroke-width="1.8">
        <rect x="4" y="6" width="20" height="18" rx="2"/><path d="M4 11h20M9 3v5M19 3v5"/><path d="M10 17l3 3 5-5"/>
      </svg>
    </div>
    <h3>Easy access</h3>
    <p>Book and be seen<br>from anywhere<br>in BC.</p>
  </div>
  <div class="benefit" style="left:183px">
    <div class="benefit-icon">
      <svg width="28" height="28" viewBox="0 0 28 28" fill="none" stroke="#0677BA" stroke-width="1.8" stroke-linecap="round">
        <path d="M12 24v-11a2 2 0 0 1 4 0v5l4 1a2 2 0 0 1 1.5 2.3L21 24"/><path d="M8 9a6 6 0 0 1 12 0M14 2v2M6 4l1.5 1.5M22 4l-1.5 1.5"/>
      </svg>
    </div>
    <h3>Effortless booking</h3>
    <p>Tap your<br>Bright Path Card<br>to begin.</p>
  </div>
  <div class="benefit" style="left:342px">
    <div class="benefit-icon">
      <svg width="28" height="28" viewBox="0 0 28 28" fill="none" stroke="#0677BA" stroke-width="1.8">
        <rect x="5" y="5" width="18" height="18" rx="3"/><path d="M14 9v10M9 14h10"/>
      </svg>
    </div>
    <h3>Trusted physicians</h3>
    <p>Licensed BC<br>family doctors.</p>
  </div>

  <div class="abs howbox">
    <div class="howbox-lead">
      <div class="kicker"><span>Convenient</span><br><span>Care</span> for<br>Common<br>Concerns</div>
      <div class="big">VIRTUAL</div>
      <div class="small">walk-in care for<br>British Columbia.</div>
    </div>
    <div class="howbox-tab"><span>How it Works</span></div>
    <div class="howbox-list">
      <div class="how-step" style="top:20px">
        <div class="step-num">1</div>
        <div><h4>Book your visit</h4><p>Choose your preferred time.</p></div>
      </div>
      <div class="how-rule" style="top:60px"></div>
      <div class="how-step" style="top:67px">
        <div class="step-num">2</div>
        <div><h4>Join the queue</h4><p>You'll be called when it's your turn.</p></div>
      </div>
      <div class="how-rule" style="top:107px"></div>
      <div class="how-step" style="top:115px">
        <div class="step-num">3</div>
        <div><h4>Speak directly with your doctor</h4><p>Simple, secure, and stress-free.</p></div>
      </div>
    </div>
  </div>

  <div class="abs brand-mark">Bright Path</div>
  <div class="abs contact">Website + Contact<br>Coming soon: brightpath-example.test</div>
</section>

</body>
</html>
```